Mobile Lime Strike Laser Tag Party Rental

I am a newbie to e-commerce and website development. I need website designed for my Mobile Lime Strike Laser Tag party rental business. I have already developed my company Logo and therefore I am looking to maximize my branding. Therefore, I have put some concept Ideas into a powerpoint presentation to sort of help promote some creativity (since I am not creative). What I am looking for is a site that I can take and continue to develop as time passes. I need the site to be highly interactive (I do not want static site) would like plenty of movement and clickable interaction/ sound is a plus. With plenty of Pictures (some I will provide at later date). The site should be informative as well as a platform for customers to be able to schedule an event and also make the necessary payment right online (call to action). I would like for the site to have a picture/video gallery for media that i will collect at a later date after providing services for my customers. (Also, Picutures can be used/not used or manipulate however creative you can be)

Reason: In order to get project ideas and completion

Target Market(s)

Ages 8-40

Primarily Teens (Video Gamers) Paintball & Airsoft players

Extreme Sports Fans/Live Action Gamers

College Students/Youth Groups

Corporate Managers and Team Leaders

Industry/Entity Type

E-Commerce

Requirements
Must have
• My Logos (I'll provide)
• My Color Scheme (Black, Ultra Lime Green (nearly Flourescent), Metallic Grey/Aluminum or Silver
• My Tag Line " Let's Get Tag-tical ! "
• Email/Phone/Birthday/Age Request forms for collection purposes
• Must have ability to make online payment
• Ability for customers to leave comments/or reviews
• links to social media
Should not have
• Should not be static (No Sound or No movement)

```html
<!DOCTYPE html>
<html lang="en">
<head>
<meta charset="utf-8">
<title>Lime Strike Laser Tag</title>
<link href="https://fonts.googleapis.com/css2?family=Oswald:wght@400;500&family=Roboto:ital,wght@0,400;1,400&display=swap" rel="stylesheet">
<style>
:root{
  --lime:#3fc21f;
  --lime-bright:#45d024;
  --ink:#0a0a0a;
  --page:#1b1b1b;
  --panel:#2a2a2a;
  --box:#333333;
  --bar:#1e1e1e;
  --text:#cfcfcf;
  --muted:#8d8d8d;
  --silver:#bdbdbd;
  --line:#444444;
}
*{margin:0;padding:0;box-sizing:border-box}
html,body{width:892px;height:1200px;overflow:hidden}
body{position:relative;background:radial-gradient(circle at 30% 60%,#2a2a2a 0,#161616 70%);font-family:"Roboto",Arial,sans-serif;color:var(--text)}
.abs{position:absolute}

.masthead{left:0;top:0;width:892px;height:104px;background:var(--ink)}
.brand{left:134px;top:40px;display:flex;align-items:center;gap:8px}
.brand-mark{width:14px;height:14px;border-radius:50%;background:var(--lime)}
.brand-name{font-family:"Oswald",sans-serif;font-weight:400;font-size:16px;color:var(--lime);letter-spacing:1px}
.site-title{left:277px;top:38px;font-family:"Oswald",sans-serif;font-weight:400;font-size:21px;color:#fff;letter-spacing:1px}
.book-btn{left:601px;top:34px;width:142px;height:33px;border-radius:4px;background:linear-gradient(#dcdcdc,#9a9a9a);border:1px solid #777;display:flex;align-items:center;justify-content:center;gap:8px;font-family:"Oswald",sans-serif;font-size:12px;color:#555}

.category-bar{left:0;top:104px;width:892px;height:46px;background:linear-gradient(#2b2b2b,#1d1d1d);border-top:1px solid #3a3a3a;display:flex;justify-content:center;align-items:center}
.category-bar ul{list-style:none;display:flex;width:624px;justify-content:space-between;font-family:"Oswald",sans-serif;font-size:9px;color:#e6e6e6}

.main-nav{left:0;top:150px;width:892px;height:59px;background:linear-gradient(#262626,#1a1a1a);border-top:1px solid #3a3a3a}
.main-nav ul{position:absolute;left:134px;top:0;height:59px;list-style:none;display:flex;font-family:"Oswald",sans-serif;font-size:11px;color:#eee}
.main-nav li{height:59px;display:flex;align-items:center;justify-content:center;border-right:1px solid #111;box-shadow:1px 0 0 #333}
.main-nav li.current{background:radial-gradient(ellipse at 50% 0,#6a5a40 0,#2c2c2c 45%,#232323 100%)}

.hero{left:134px;top:209px;width:624px;height:304px;background:linear-gradient(110deg,#3a3a3a 0,#1f2426 45%,#5a5e62 75%,#2e3134 100%)}
.hero-arrow{width:24px;height:24px;border-radius:50%;border:2px solid #bbb;display:flex;align-items:center;justify-content:center}

.content{left:134px;top:513px;width:624px;height:618px;background:var(--panel)}
.call-label{left:151px;top:527px;font-family:"Oswald",sans-serif;font-size:11px;color:#ddd}
.call-number{left:151px;top:541px;font-family:"Oswald",sans-serif;font-size:17px;color:var(--lime)}
.side-box{left:150px;width:168px;background:var(--box);border:1px solid #3d3d3d;padding:12px 15px}
.side-box h3{font-family:"Oswald",sans-serif;font-weight:400;font-size:14px;color:var(--lime);margin-bottom:4px}
.green-btn{display:flex;align-items:center;justify-content:center;height:22px;background:linear-gradient(var(--lime-bright),#2ea313);color:#fff;font-size:9px}
.card{width:28px;height:18px;border-radius:2px;background:#d9d9d9}
.news-item{border-bottom:1px solid #444;padding:6px 0 8px}
.news-item:last-child{border-bottom:none}
.news-date{font-size:6.5px;font-style:italic;color:var(--lime);margin-bottom:5px}
.news-text{font-size:6.5px;line-height:11px;color:var(--muted)}
.links li{list-style:none;font-size:7px;color:var(--muted);display:flex;align-items:center;gap:8px;height:19px}

.section-title{font-family:"Oswald",sans-serif;font-weight:400;font-size:16px;color:var(--lime)}
.body-copy{font-size:6.5px;line-height:14px;color:var(--muted)}
.divider{height:1px;background:var(--line)}
.video{left:345px;top:793px;width:200px;height:141px;background:radial-gradient(circle at 50% 40%,#7dff4a 0,#2fa10f 40%,#0c3a06 100%)}
.video-bar{position:absolute;left:0;bottom:0;width:200px;height:16px;background:#1a1a1a;display:flex;align-items:center;gap:6px;padding:0 5px;font-size:6px;color:#ccc}
.thumb{top:998px;height:102px;background:#3a3a3a;padding:5px}
.thumb div{width:100%;height:100%}

.footer{left:134px;top:1131px;width:624px;height:69px;background:#111}
.rating-badge{left:144px;top:1144px;width:34px;height:42px;background:#e8e8e8;border:2px solid #333}
.footer-links{left:195px;top:1148px;display:flex;gap:10px;font-size:6.5px;color:#bbb}
.copyright{left:195px;top:1170px;font-size:6.5px;color:#aaa}
.follow{left:612px;top:1161px;font-size:6px;color:#aaa}
.social{top:1157px;width:15px;height:15px;border-radius:50%;background:#6d7480}
</style>
</head>
<body>

<header class="masthead abs">
  <div class="brand abs"><span class="brand-mark"></span><span class="brand-name">LIME STRIKE</span></div>
  <div class="site-title abs">LIME STRIKE LASER TAG</div>
  <a class="book-btn abs">
    <svg width="18" height="14" viewBox="0 0 18 14" aria-hidden="true"><rect x="1" y="1" width="16" height="9" fill="none" stroke="#555" stroke-width="1.5"/><rect x="6" y="11" width="6" height="2" fill="#555"/></svg>
    BOOK ONLINE
  </a>
</header>

<nav class="category-bar abs">
  <ul>
    <li>BIRTHDAY PARTIES</li><li>SCHOOL/COLLEGE PARTIES</li><li>CORPORATE EVENTS</li><li>MILITARY GROUPS</li><li>FUNDRAISERS</li><li>CHURCH GROUPS</li><li>SUMMER CAMPS</li>
  </ul>
</nav>

<nav class="main-nav abs">
  <ul>
    <li class="current" style="width:84px">HOME</li>
    <li style="width:101px">GALLERIES</li>
    <li style="width:153px">PARTY/EVENT PACKAGES</li>
    <li style="width:93px">ARMOREY</li>
    <li style="width:78px">F.A.Q</li>
    <li style="width:108px">ABOUT US</li>
  </ul>
</nav>

<section class="hero abs" role="img" aria-label="Banner illustration of a player aiming a laser tag blaster beside a metallic game title plate"></section>
<div class="hero-arrow abs" style="left:144px;top:352px"><svg width="10" height="10" viewBox="0 0 10 10"><path d="M7 1 L2 5 L7 9" fill="none" stroke="#ddd" stroke-width="1.5"/></svg></div>
<div class="hero-arrow abs" style="left:726px;top:352px"><svg width="10" height="10" viewBox="0 0 10 10"><path d="M3 1 L8 5 L3 9" fill="none" stroke="#ddd" stroke-width="1.5"/></svg></div>
<svg class="abs" style="left:696px;top:481px" width="50" height="18" viewBox="0 0 50 18" aria-hidden="true">
  <path d="M10 2 L4 9 L10 16" fill="none" stroke="#bbb" stroke-width="1.5"/>
  <path d="M36 2 L42 9 L36 16" fill="none" stroke="#bbb" stroke-width="1.5"/>
</svg>

<main class="content abs"></main>

<div class="call-label abs">CALL US AT :</div>
<div class="call-number abs">(555) 014 - 2290</div>

<aside class="side-box abs" style="top:576px;height:113px">
  <h3>BOOK ONLINE</h3>
  <p style="font-size:6.5px;font-style:italic;color:#ddd;margin-bottom:9px">Reserve your Campaign now it!!!</p>
  <div class="green-btn">Checkout using&nbsp;<span style="font-size:11px">QuickPay</span>&nbsp;›</div>
  <div style="display:flex;gap:7px;margin:9px 0 0 9px"><span class="card"></span><span class="card"></span><span class="card"></span><span class="card"></span></div>
</aside>

<aside class="side-box abs" style="top:701px;height:185px">
  <h3>NEWS &amp; EVENTS</h3>
  <div class="news-item"><p class="news-date">Posted on &nbsp;24 Jun 2013</p><p class="news-text">uncover many web sites still in their infancy.<br>Various versions have evolved...</p></div>
  <div class="news-item"><p class="news-date">Posted on &nbsp;24 Jun 2013</p><p class="news-text">uncover many web sites still in their infancy.<br>Various versions have evolved...</p></div>
  <div class="news-item"><p class="news-date">Posted on &nbsp;24 Jun 2013</p><p class="news-text">uncover many web sites still in their infancy.<br>Various versions have evolved...</p></div>
</aside>

<aside class="side-box abs" style="top:899px;height:73px">
  <h3 style="margin-bottom:8px">EVERY ONE DISCOUNTS</h3>
  <div class="green-btn">Click here to find out more</div>
</aside>

<aside class="side-box abs" style="top:983px;height:119px">
  <h3 style="margin-bottom:6px">HELP FULL LINKS</h3>
  <ul class="links">
    <li><svg width="9" height="8" viewBox="0 0 9 8"><path d="M1 4 L3.5 6.5 L8 1" fill="none" stroke="#3fc21f" stroke-width="1.6"/></svg>Parental Consent &amp; Waiver Form</li>
    <li><svg width="9" height="8" viewBox="0 0 9 8"><path d="M1 4 L3.5 6.5 L8 1" fill="none" stroke="#3fc21f" stroke-width="1.6"/></svg>Read Reviews &amp; Comments</li>
    <li><svg width="9" height="8" viewBox="0 0 9 8"><path d="M1 4 L3.5 6.5 L8 1" fill="none" stroke="#3fc21f" stroke-width="1.6"/></svg>Parental Consent &amp; Waiver Form</li>
    <li><svg width="9" height="8" viewBox="0 0 9 8"><path d="M1 4 L3.5 6.5 L8 1" fill="none" stroke="#3fc21f" stroke-width="1.6"/></svg>Read Reviews &amp; Comments</li>
  </ul>
</aside>

<h2 class="section-title abs" style="left:342px;top:538px">WELCOME TO LIME STRIKE LASER TAG</h2>
<p class="body-copy abs" style="left:345px;top:569px;width:400px">It is a long established fact that a reader will be distracted by the readable content of a page when looking at its layout. The point of using Lorem Ipsum is that it has a more-or-less normal distribution of letters, as opposed to using 'Content here, content here', making it look like readable English. Many desktop publishing packages and web page editors now use Lorem Ipsum as their default model text, and a search for 'lorem ipsum' will uncover many web sites still in their infancy. Various versions have evolved over the years, sometimes by accident, sometimes on purpose.their default model text, and a search for 'lorem ipsum' will uncover many web sites still in their infancy. Various versions have evolved over the years, sometimes by accident, sometimes on purpose their default model text, and a search for 'lorem ipsum' will uncover many web sites still in their infancy. Various versions have evolved over the years, sometimes by accident, sometimes on purpose.</p>
<p class="body-copy abs" style="left:345px;top:695px;width:400px">It is a long established fact that a reader will be distracted by the readable content of a page when looking at its layout. The point of using Lorem Ipsum is that it has a more-or-less normal distribution of letters, as opposed to using 'Content here, content here', making it look like readable English. Many desktop publishing packages and web page editors now use Lorem Ipsum as their default model text, and a search for 'lorem ipsum' will uncover...</p>
<div class="divider abs" style="left:345px;top:772px;width:400px"></div>

<div class="video abs" role="img" aria-label="Promo video still with a glowing green burst">
  <svg class="abs" style="left:86px;top:50px" width="28" height="28" viewBox="0 0 28 28" aria-hidden="true"><circle cx="14" cy="14" r="13" fill="rgba(0,0,0,.35)" stroke="#ddd" stroke-width="1.5"/><path d="M11 8 L20 14 L11 20Z" fill="#ddd"/></svg>
  <div class="video-bar"><span>❚❚</span><span>◀)</span><span>0:04 / 0:30</span><span style="flex:1;height:3px;background:#444;position:relative"><span style="position:absolute;left:0;top:0;width:14px;height:3px;background:#c22"></span></span><span>⤢</span></div>
</div>
<h2 class="section-title abs" style="left:572px;top:797px">OUR VIDEOS</h2>
<p class="body-copy abs" style="left:575px;top:823px;width:172px">It is a long established fact that a reader will be distracted by the readable content of a page when looking at its layout. The point of using Lorem Ipsum is that it has a more-or-less normal distribution of letters, as opposed to using 'Content here, content here', making it look like readable English. Many desktop publishing packages and web page editors...</p>
<div class="divider abs" style="left:345px;top:953px;width:400px"></div>

<h2 class="section-title abs" style="left:345px;top:966px">OUR GALLERY</h2>
<svg class="abs" style="left:718px;top:975px" width="27" height="13" viewBox="0 0 27 13" aria-hidden="true"><rect width="13" height="13" fill="#444"/><rect x="14" width="13" height="13" fill="#444"/><path d="M8 3 L5 6.5 L8 10" fill="none" stroke="#999"/><path d="M19 3 L22 6.5 L19 10" fill="none" stroke="#999"/></svg>
<div class="thumb abs" style="left:345px;width:127px"><div role="img" aria-label="Photo of young players in tactical vests outdoors" style="background:linear-gradient(#7a8a6a,#3f4a3a)"></div></div>
<div class="thumb abs" style="left:482px;width:127px"><div role="img" aria-label="Photo of a player taking cover behind a tree" style="background:linear-gradient(#8a7a5a,#4a4634)"></div></div>
<div class="thumb abs" style="left:618px;width:127px"><div role="img" aria-label="Photo of a player holding a blaster on a blue grid backdrop" style="background:linear-gradient(#2c8fb4,#173c52)"></div></div>

<footer class="footer abs"></footer>
<div class="rating-badge abs"></div>
<div class="footer-links abs"><span>HOME</span><span>|</span><span>GALLERIES</span><span>|</span><span>PARTY/EVENT PACKAGES</span><span>|</span><span>ARMOREY</span><span>|</span><span>F.A.Q</span><span>|</span><span>ABOUT US</span></div>
<div class="copyright abs">COPYRIGHT © 2014. <span style="color:var(--lime)">LIME STRIKE LASER TAG</span>. ALL RIGHTS RESERVED.</div>
<div class="follow abs">FOLLOW US :</div>
<span class="social abs" style="left:654px"></span>
<span class="social abs" style="left:673px"></span>
<span class="social abs" style="left:692px"></span>
<span class="social abs" style="left:711px"></span>
<span class="social abs" style="left:731px"></span>

</body>
</html>
```